Velnet Website

We need a website for a new Telecommunications company based in Australia. Our service is offered to people who are in the middle of moving properties as our major channel partners relocate renters and home owners. The website will outline the products we sell, which will include pricing as well as provide information for people who are in the middle of a move. Our client base will not come from any demographic, however 95% will be people renting properties and therefore most likely range in age from 18 and upwards. I would like to have an energetic feel to the website with a young theme. It needs full integration with Social Media, must be mobile centric as well, must include video as well as have chat options for visitors and be as interactive as possible . It should not be too cluttered as it needs to be clean and feel fresh. People who are moving are time poor and stressed (I am sure you have all moved!) and therefore our service needs to be complimentary and simple for them to engage with. We have a channel passing hot leads for this purpose, however we would like to market our services to others outside of this channel. We are offering most services such as home phone, internet and prepaid mobiles as unlimited services to make things simple and easy to commit to. Logo at this stage is Red, however we also need soothing colours on the site. I like the website layout of Plumora.com as an example, as it is clean and delivers the type of feel we are after. Your design does not have to mimic it, it just needs to give off the same feel.
Updates

Specific Competitors websites include the following:

http://www.brightkestrel.com.au/
http://www.lanternpoint.com.au/index.asp
http://gravelbay.com.au/
http://www.silvanhoist.com.au/

Our site needs to be far more interactive than these.  Chat prompts once someone is on the site would be useful - asking "Are you ready to move?" "Do you want everything unlimited?" - click to chat, etc.

Hi Designers,

Could you please look at making the designs more Telecommunications focused.  Our primary focus is to move peoples phone services, so the Telco component and Broadband and internet is a key component.  The moving information is good, however none of the designs addresses the Telecommunications part, I want it clear that when someone comes to the site they can get a new fixed line, internet and pre paid mobile phone plan.

Thanks

Ned

Target Market(s)

People moving property who want to get their telecommunication and internet services connected at their new place.

Industry/Entity Type

Internet

Requirements
Must have
• Social Media
Video section
How to section
Pricing section
Moving information section
Useful links section
Live chat

```html
<!DOCTYPE html>
<html lang="en">
<head>
<meta charset="utf-8">
<title>Velnet – Telecommunication</title>
<link href="https://fonts.googleapis.com/css2?family=PT+Sans:ital,wght@0,400;0,700;1,400&family=Ubuntu:wght@400;500&display=swap" rel="stylesheet">
<style>
:root{
  --red:#e2000f;
  --red-dark:#b8000b;
  --ink:#222;
  --text:#333;
  --muted:#8a8a8a;
  --line:#e1e1e1;
  --soft:#f3f3f3;
  --footer:#f0f0f0;
  --icon:#6b6b6b;
}
*{box-sizing:border-box;margin:0;padding:0}
html,body{width:833px;height:1200px;overflow:hidden;background:#fff}
body{position:relative;font-family:"PT Sans",sans-serif;color:var(--text);font-size:9px;line-height:1.6}
a{color:inherit;text-decoration:none}
.abs{position:absolute}

/* header */
.site-header{position:absolute;left:0;top:0;width:833px;height:108px;background:linear-gradient(#ececec 0 3px,#fafafa 3px,#f4f4f4)}
.brand{position:absolute;left:24px;top:22px;display:flex;align-items:center;gap:8px}
.brand-mark{width:22px;height:22px;border-radius:50%;background:var(--red)}
.brand-name{font-family:"Ubuntu",sans-serif;font-weight:500;font-size:26px;color:var(--red);letter-spacing:.5px}
.utility-links{position:absolute;right:25px;top:10px;font-size:9px;color:#666}
.utility-links span{margin:0 4px;color:#aaa}
.social{display:flex;gap:6px}
.social i{display:block;width:17px;height:17px;border-radius:50%;background:var(--icon)}
.header-social{position:absolute;right:27px;top:43px}
.call{position:absolute;right:20px;top:72px;font-family:"Ubuntu",sans-serif;font-size:15px;color:#666}
.call b{font-weight:400;color:var(--ink);margin-left:4px}

/* nav */
.main-nav{position:absolute;left:0;top:108px;width:833px;height:41px;background:linear-gradient(var(--red),#d4000d);display:flex;font-family:"Ubuntu",sans-serif;font-size:11.5px;color:#fff}
.main-nav a{height:41px;line-height:41px;text-align:center;border-right:1px solid rgba(0,0,0,.18)}
.live-chat{position:absolute;right:0;top:0;width:153px;height:41px;display:flex;align-items:center;justify-content:center;gap:7px;border-left:1px solid rgba(0,0,0,.18)}

/* hero */
.hero{position:absolute;left:0;top:149px;width:833px;height:298px;background:linear-gradient(90deg,#c8cdd3 0%,#d9b9a5 22%,#dcc4b5 35%,#c7d3de 60%,#b6c6d6 100%)}
.hero-card{position:absolute;left:439px;top:76px;width:360px;height:98px;background:#fff;padding:14px 22px;box-shadow:0 1px 4px rgba(0,0,0,.15)}
.hero-card h2{font-family:"Ubuntu",sans-serif;font-weight:400;font-size:15.5px;line-height:1.2;color:var(--ink)}
.hero-card h1{font-family:"Ubuntu",sans-serif;font-weight:400;font-size:22px;line-height:1.2;color:var(--ink)}
.hero-card p{font-size:12.5px;color:var(--red);margin-top:3px}

/* welcome */
.section-title{font-family:"Ubuntu",sans-serif;font-weight:400;font-size:13.5px;color:var(--red)}
.welcome{position:absolute;left:21px;top:463px;width:485px}
.welcome-image{position:absolute;left:2px;top:31px;width:184px;height:102px;border:1px solid #ccc;background:linear-gradient(135deg,#8ec3ea,#cfe4f5 55%,#6d7785)}
.welcome-lead{position:absolute;left:198px;top:28px;width:290px;font-size:9.5px;color:var(--ink)}
.welcome-lead p+p{margin-top:4px;font-size:8.8px;color:var(--text)}
.welcome-body{position:absolute;left:0;top:141px;width:485px;font-size:8.8px}
.welcome-body p+p{margin-top:4px}
.video{position:absolute;left:523px;top:463px}
.video-player{position:absolute;left:0;top:28px;width:284px;height:197px;background:radial-gradient(circle at 50% 45%,#3a3a3a,#000 70%)}
.progress{position:absolute;left:10px;right:13px;top:179px;height:2px;background:#555}
.progress i{position:absolute;left:13px;top:-3px;width:8px;height:8px;border-radius:50%;background:#fff}

/* features */
.features{position:absolute;left:0;top:736px;width:833px;height:216px;border-top:1px solid var(--line)}
.feature{position:absolute;top:0;height:212px;padding-top:26px}
.feature+.feature{border-left:1px solid var(--line)}
.feature h3{font-family:"Ubuntu",sans-serif;font-weight:400;font-size:13.5px;color:var(--ink);line-height:1.2}
.feature .tagline{font-style:italic;color:var(--muted);font-size:8.5px;margin:3px 0 8px}
.feature p{font-size:8.8px;line-height:1.65}
.feature p+p{margin-top:4px}
.btn{position:absolute;bottom:-5px;display:inline-block;background:var(--red);color:#fff;font-size:8.5px;padding:2px 7px;border-radius:2px}
.price-table{border-collapse:collapse;font-size:8.8px;margin-left:2px}
.price-table td{height:18.5px;padding:0}
.price-table td:nth-child(1){width:67px}
.price-table td:nth-child(2){width:38px;color:var(--red);font-weight:700}
.link-list{list-style:none;margin-top:11px;font-size:8.8px}
.link-list li{height:21.7px;padding-left:17px;position:relative}
.link-list li::before{content:"";position:absolute;left:5px;top:4px;border:3px solid transparent;border-left:4px solid #333}

/* footer */
.site-footer{position:absolute;left:0;top:975px;width:833px;height:184px;background:var(--footer)}
.footer-col{position:absolute;top:24px}
.footer-col h4{font-family:"Ubuntu",sans-serif;font-weight:400;font-size:12.5px;color:var(--ink);padding-bottom:3px;border-bottom:1px solid #cfcfcf;margin-bottom:6px}
.footer-col ul{list-style:none;font-size:8.8px;color:#555}
.footer-col li{height:20px}
.newsletter p{font-size:9.5px;color:#555}
.email{margin-top:5px;width:199px;height:23px;border:1px solid #d4d4d4;border-radius:3px;background:#fff;font-style:italic;font-size:8.5px;color:#777;padding:4px 8px}
.subscribe{margin:5px 0 0 131px;width:69px;height:22px;background:var(--red);color:#fff;border-radius:2px;font-size:10.5px;text-align:center;line-height:22px}
.bottom-bar{position:absolute;left:0;top:1159px;width:833px;height:41px;background:#e9e9e9;border-top:1px solid #ddd;font-size:8.8px;color:#555;padding:10px 20px}
.bottom-bar span{color:#999;margin:0 4px}
</style>
</head>
<body>

<header class="site-header">
  <a class="brand" href="#"><span class="brand-mark"></span><span class="brand-name">Velnet</span></a>
  <nav class="utility-links"><a href="#">Support</a><span>|</span><a href="#">FAQ</a><span>|</span><a href="#">Location</a><span>|</span><a href="#">Sitemap</a></nav>
  <div class="social header-social" aria-label="Social media"><i></i><i></i><i></i><i></i></div>
  <div class="call">Call Us <b>+61 1300 555 214</b></div>
</header>

<nav class="main-nav">
  <a href="#" style="width:82px">HOME</a>
  <a href="#" style="width:118px">HOW WE WORK</a>
  <a href="#" style="width:86px">SERVICES</a>
  <a href="#" style="width:107px">OUR PRICING</a>
  <a href="#" style="width:112px">INFORMATION</a>
  <a href="#" style="width:82px">SUPPORT</a>
  <a href="#" style="width:93px">CONTACT</a>
  <a href="#" class="live-chat">
    <svg width="22" height="20" viewBox="0 0 22 20"><ellipse cx="9" cy="8" rx="8" ry="6.5" fill="#fff"/><path d="M4 12 L3 18 L9 14Z" fill="#fff"/><ellipse cx="15" cy="12" rx="6" ry="5" fill="#fff" stroke="#d4000d" stroke-width="1.2"/></svg>
    Live Chat
  </a>
</nav>

<section class="hero" role="img" aria-label="Photo of a smiling young man talking on a mobile phone">
  <div class="hero-card">
    <h2>GET IN TOUCH FROM EVERY ONE WITH</h2>
    <h1>OUR TELE COMMUNICATION</h1>
    <p>Lorem ipsum dolor sit amet, consectetuer adipiscing elit.</p>
  </div>
</section>

<section class="welcome">
  <h2 class="section-title">Welcome to Velnet Website Mainpage</h2>
  <div class="welcome-image" role="img" aria-label="Hand holding a mobile phone over a world map with network lines"></div>
  <div class="welcome-lead">
    <p>Lorem ipsum dolor sit amet, consectetuer adipiscing elit. Nam cursus. Morbi ut mi.</p>
    <p>Mauris vel lacus vitae felis vestibulum volutpat. Etiam est nunc, venenatis in, tristique eu, imperdiet ac, nisl. Cum sociis natoque penatibus et magnis dis parturient montes, nascetur ridiculus mus. In iaculis facilisis massa. Etiam eu urna. Sed porta. Suspendisse quam leo, molestie sed, luctus quis, feugiat in, pede.</p>
  </div>
  <div class="welcome-body">
    <p>Pellentesque habitant morbi tristique senectus et netus et malesuada fames ac turpis egestas. In posuere felis nec tortor. Pellentesque faucibus. Ut accumsan ultricies elit. Maecenas at justo id velit placerat molestie. Donec dictum lectus non odio. Cras a ante vitae enim iaculis aliquam.</p>
    <p>Mauris nunc quam, venenatis nec, euismod sit amet, egestas placerat, est. Pellentesque habitant morbi tristique senectus et netus et malesuada fames ac turpis egestas. Cras id elit. Integer quis urna. Ut ante enim, dapibus malesuada, fringilla eu, condimentum quis, tellus.</p>
  </div>
</section>

<section class="video">
  <h2 class="section-title">Latest Video</h2>
  <div class="video-player">
    <svg class="abs" style="left:128px;top:76px" width="30" height="34" viewBox="0 0 30 34"><path d="M2 1 L28 17 L2 33Z" fill="#fff"/></svg>
    <div class="progress"><i></i></div>
  </div>
</section>

<section class="features">
  <div class="feature" style="left:0;width:216px;padding-left:29px;padding-right:12px">
    <h3>Moving Information</h3>
    <div class="tagline">Moving Information tittle line goes with it</div>
    <p>Lorem ipsum dolor sit amet, consectetuer adipiscing elit. Nam cursus. Morbi ut mi. Nullam enim leo, egestas id, condimentum at, laoreet mattis, massa.</p>
    <p>Sed eleifend nonummy diam. Praesent mauris ante, elementum et, bibendum at, posuere sit amet, nibh.</p>
    <a class="btn" href="#">learn more</a>
  </div>
  <div class="feature" style="left:216px;width:197px;padding-left:27px">
    <h3>Pricing section</h3>
    <div class="tagline">Pricing Section tittle line goes with it</div>
    <table class="price-table">
      <tr><td>Plan Name</td><td>30$</td><td>1 months</td></tr>
      <tr><td>Plan Name</td><td>50$</td><td>2 months</td></tr>
      <tr><td>Plan Name</td><td>60$</td><td>2 months</td></tr>
      <tr><td>Plan Name</td><td>80$</td><td>3 months</td></tr>
      <tr><td>Plan Name</td><td>90$</td><td>3 months</td></tr>
      <tr><td>Plan Name</td><td>200$</td><td>4 months</td></tr>
    </table>
    <a class="btn" href="#">more price</a>
  </div>
  <div class="feature" style="left:413px;width:211px;padding-left:24px;padding-right:14px">
    <h3>How to Section</h3>
    <div class="tagline">How it&nbsp; Information tittle line goes with it</div>
    <p>Lorem ipsum dolor sit amet, consectetuer adipiscing elit. Nam cursus. Morbi ut mi. Nullam enim leo, egestas id, condimentum at, laoreet mattis, massa.</p>
    <p>Sed eleifend nonummy diam. Praesent mauris ante, elementum et, bibendum at, posuere sit amet, nibh.</p>
    <a class="btn" href="#">learn more</a>
  </div>
  <div class="feature" style="left:624px;width:209px;padding-left:20px">
    <h3>Useful links</h3>
    <div class="tagline">Sites usefull&nbsp; links line goes with it</div>
    <ul class="link-list">
      <li>Company Overview</li><li>How We Work</li><li>Featured Services</li><li>Our Pricing Section</li><li>Contact Information</li>
    </ul>
  </div>
</section>

<footer class="site-footer">
  <div class="footer-col newsletter" style="left:29px;width:200px">
    <h4>Newsletters Sign up</h4>
    <p>Please sign up here for latest newslettes</p>
    <div class="email">email address</div>
    <div class="subscribe">Subscribe</div>
  </div>
  <div class="footer-col" style="left:278px;width:106px">
    <h4>Company</h4>
    <ul><li>About Company</li><li>Why We Are</li><li>How its Work</li><li>Features</li><li>Recent Blog</li></ul>
  </div>
  <div class="footer-col" style="left:402px;width:106px">
    <h4>Support</h4>
    <ul><li>News &amp; update</li><li>Video</li><li>Pricing Section</li><li>Moving Information</li><li>Usefull links</li></ul>
  </div>
  <div class="footer-col" style="left:530px;width:105px">
    <h4>Contact</h4>
    <ul><li>Live Chat</li><li>Locations</li><li>Get in Touch</li><li>Contact info</li></ul>
  </div>
  <div class="footer-col" style="left:666px;width:137px">
    <h4>Stay Connected</h4>
    <ul><li>Get in touch with us every time</li></ul>
    <div class="social" style="margin-top:6px;gap:8px"><i style="width:20px;height:20px"></i><i style="width:20px;height:20px"></i><i style="width:20px;height:20px"></i><i style="width:20px;height:20px"></i></div>
  </div>
</footer>

<div class="bottom-bar">© 2012 Company Name<span>|</span>All right reserved<span>|</span>Term &amp; Conditions</div>

</body>
</html>
```